New Equipment Rental Location Postcard *

We have a new equipment rental location that we opened and want to do a bulk mailing with a postcard to advertise. The post card has to be 6.5" x 9" and printed on both sides. The back side has to have the postage icons on them like in the example postcard I have uploaded. Also I have included our logo in the attachments. The attachement "capture' is just an example of how the back should look with the 2 postage icons. I have also uploaded those 2 graphics.

Industry/Entity Type

Rental

Requirements
Must have
• I would like to convey "New Location". Also would like our customers to know that our rental fleet consists of "Well Maintained and New Equipment". Also would like to say that we will beat any competitors price. Also on the back, I want to include a 10% discount coupon (almost like the postcard I included as an example.
• Lastly if you could list the following industries that we provide rentals for:
• Landscape / Tree Professionals
• Contractors
• Do-It-yourself'ers
• Home and Office Supplies
Nice to have
• If we could find somewhere to list that we ALSO have 60' bucket/chipper trucks, as well as 12", 14", & 18" chippers for rent at an affordable price that would be great.
• As some of the backdrops we could incorporate Dov Skid Steers, Plavek Power tools, as well as Brennacourt bucket trucks and Dulsant chippers. I have attached some pictures as examples. We don't have to use these, just some ideas. I would like to show some pictures to show the equipment we rent (like the attached ones)

```html
<!DOCTYPE html>
<html lang="en">
<head>
<meta charset="utf-8">
<title>Fieldline Rentals – New Location Postcard</title>
<link href="https://fonts.googleapis.com/css2?family=Michroma&family=Open+Sans:ital,wght@0,400;0,600;0,700;1,400&family=Oswald:wght@500;600&display=swap" rel="stylesheet">
<style>
  :root{
    --navy:#1d4470;
    --navy-dark:#163659;
    --orange:#f6b35a;
    --gray:#8a8c8f;
    --gray-band:#9a9c9f;
    --text-gray:#6b6d70;
    --paper:#ffffff;
    --paper-soft:#f1f2f2;
    --stage:#e9e9ea;
  }
  *{box-sizing:border-box;margin:0;padding:0}
  html,body{width:809px;height:1200px;overflow:hidden;background:var(--stage)}
  .stage{position:relative;width:879px;height:1304px;transform:scale(0.9204);transform-origin:0 0}
  .card{position:absolute;width:701px;height:500px;background:var(--paper);overflow:hidden;box-shadow:0 6px 14px rgba(0,0,0,.25);font-family:"Open Sans",Arial,sans-serif}
  .card--front{left:80px;top:75px;background:var(--paper-soft)}
  .card--back{left:78px;top:715px}
  .abs{position:absolute}

  /* brand */
  .brand{display:flex;align-items:center;gap:8px}
  .brand__dot{width:16px;height:16px;border-radius:50%;background:var(--orange);flex:none}
  .brand__name{font-family:"Open Sans",Arial,sans-serif;font-weight:700;font-size:25px;line-height:1;letter-spacing:.5px}
  .brand__sub{font-family:"Open Sans",Arial,sans-serif;font-weight:700;font-size:12px;letter-spacing:3px;margin-top:4px}

  /* front */
  .front-photo{left:290px;top:0;width:411px;height:430px}
  .badge{left:218px;top:15px;width:96px;height:96px;border-radius:50%;background:var(--navy);border:3px solid var(--paper);box-shadow:0 0 0 2px var(--navy);text-align:center;color:#fff;font-family:"Oswald",sans-serif;font-weight:500;font-size:17px;line-height:19px;padding-top:14px}
  .badge__map{display:block;margin:6px auto 0;width:54px;height:26px;background:linear-gradient(135deg,#e9eef0,#b9d7a8);border-radius:2px}
  .equip-bar{left:0;top:123px;width:355px;height:28px;background:var(--navy);color:#fff;font-family:"Michroma",sans-serif;font-size:11.2px;line-height:28px;padding-left:18px}
  .markets{left:28px;top:168px;list-style:none}
  .markets li{display:flex;align-items:center;gap:8px;font-weight:700;font-size:14.4px;color:var(--text-gray);height:25.5px}
  .markets svg{flex:none}
  .extra-band{left:0;top:288px;width:345px;height:78px;background:var(--gray-band);color:#fff;font-style:italic;font-size:13.6px;line-height:19px;padding:7px 0 0 17px}
  .contact-label{left:24px;top:393px;height:21px;background:var(--navy);color:#fff;font-family:"Michroma",sans-serif;font-size:10.5px;line-height:21px;padding:0 12px}
  .contact-line{left:24px;display:flex;align-items:center;gap:6px;color:var(--navy);font-style:italic;font-size:18px}
  .contact-line--mail{font-size:15.5px}
  .thumb{top:370px;height:92px;border:3px solid #fff;box-shadow:0 1px 4px rgba(0,0,0,.4)}
  .front-web{right:10px;top:470px;color:#fff;font-family:"Michroma",sans-serif;font-size:16px;display:flex;align-items:center;gap:6px}
  .price-claim{left:470px;top:30px;width:220px;text-align:center;color:var(--navy);font-family:"Michroma",sans-serif;font-size:13.6px;line-height:18px}

  /* back */
  .back-photo{left:0;top:110px;width:372px;height:350px}
  .back-head{left:0;top:0;width:380px;height:130px}
  .head-brand{left:18px;top:40px;color:#fff}
  .head-copy{left:168px;top:26px;width:185px;text-align:center}
  .head-copy__lead{color:#fff;font-family:"Michroma",sans-serif;font-size:11.4px;line-height:16px}
  .head-copy__new{color:var(--orange);font-family:"Oswald",sans-serif;font-weight:600;font-size:28px;line-height:38px}
  .coupon{left:33px;top:165px;width:288px;height:141px;border:2px dashed var(--orange);background:rgba(255,255,255,.9);text-align:center}
  .coupon__big{font-family:"Oswald",sans-serif;font-weight:600;color:var(--navy);font-size:72px;line-height:80px;margin-top:4px;letter-spacing:-1px}
  .coupon__note{font-size:13px;color:#333;margin-top:-6px}
  .coupon__exp{font-size:13px;font-weight:700;color:#333;margin-top:8px}
  .call{left:20px;top:320px;width:305px;text-align:center;font-size:15.5px;color:#111}
  .call-phone{left:20px;top:340px;width:305px;display:flex;justify-content:center;align-items:center;gap:6px;color:var(--navy);font-size:24px;font-weight:700}
  .hours-label{left:111px;top:383px;width:126px;height:25px;background:var(--gray);color:#fff;text-align:center;font-weight:700;font-size:13.8px;line-height:25px}
  .hours{left:20px;top:417px;width:305px;text-align:center;font-size:14px;color:#111}
  .return-addr{left:392px;top:37px;color:var(--text-gray);font-size:10.4px;line-height:15px}
  .postage{left:600px;top:28px;width:75px;height:77px;border:1px solid #333;text-align:center;font-family:Arial,sans-serif;font-size:9.6px;line-height:12px;padding-top:7px;color:#111}
  .mail-box{left:439px;top:203px;width:192px;height:77px;border:1px solid #777;font-family:Arial,sans-serif;font-size:11px;color:#111}
  .mail-box__route{position:absolute;right:14px;top:9px;font-size:8px}
  .mail-box__to{position:absolute;left:14px;top:36px;line-height:13px}
  .equip-art{left:452px;top:312px;width:175px;height:95px;border-radius:6px;background:radial-gradient(ellipse at center,#f3d34a 0%,#f6e7a2 45%,#fff 75%)}
  .back-web{left:422px;top:423px;color:var(--gray);font-family:"Michroma",sans-serif;font-size:13.2px}
  .back-foot-rule{left:0;top:450px;width:701px;height:6px;background:#a5a7aa}
  .back-foot{left:0;top:456px;width:701px;height:44px;background:var(--navy);display:flex;align-items:center;justify-content:space-between;padding:0 22px 0 15px}
  .back-foot__claim{color:#fff;font-family:"Michroma",sans-serif;font-size:14.4px}
  .socials{display:flex;gap:8px}
  .socials span{width:20px;height:20px;border-radius:50%;border:1.4px solid #fff}
</style>
</head>
<body>
<main class="stage">

  <!-- Front -->
  <section class="card card--front" aria-label="Postcard front">
    <svg class="abs front-photo" viewBox="0 0 411 430" aria-hidden="true">
      <defs>
        <linearGradient id="sky" x1="0" y1="0" x2="0" y2="1">
          <stop offset="0" stop-color="#d6e6f4"/><stop offset=".55" stop-color="#c9ccd0"/><stop offset="1" stop-color="#8d9094"/>
        </linearGradient>
      </defs>
      <path d="M95 0 H411 V430 H0 C60 330 75 120 95 0 Z" fill="url(#sky)"/>
      <path d="M95 0 C75 120 60 330 0 430 H-10 C48 330 65 120 82 0 Z" fill="var(--navy)"/>
      <path d="M110 0 C92 120 78 330 15 430 H3 C65 330 82 120 98 0 Z" fill="var(--orange)"/>
    </svg>
    <div class="abs" role="img" aria-label="Photo of a Corvane bucket truck on a Brennacourt chassis" style="left:390px;top:95px;width:311px;height:320px;background:linear-gradient(180deg,rgba(255,255,255,0) 0%,rgba(240,240,240,.75) 40%,rgba(120,122,125,.6) 100%)"></div>

    <div class="abs brand" style="left:22px;top:58px">
      <span class="brand__dot"></span>
      <div>
        <div class="brand__name" style="color:var(--navy)">FIELDLINE</div>
        <div class="brand__sub" style="color:var(--orange)">RENTALS</div>
      </div>
    </div>

    <div class="abs badge">NEW<br>LOCATION
      <span class="badge__map" role="img" aria-label="Folded map illustration"></span>
    </div>

    <div class="abs price-claim">WE WILL BEAT ANY<br>COMPETITORS PRICE</div>

    <div class="abs equip-bar">WELL MAINTAINED AND NEW EQUIPMENT</div>

    <ul class="abs markets">
      <li><svg width="11" height="11" viewBox="0 0 11 11"><rect x=".5" y=".5" width="10" height="10" fill="none" stroke="var(--navy)"/><path d="M2.5 5.5l2 2 4-5" fill="none" stroke="var(--orange)" stroke-width="1.6"/></svg>LANDSCAPE / TREE PROFESSIONALS</li>
      <li><svg width="11" height="11" viewBox="0 0 11 11"><rect x=".5" y=".5" width="10" height="10" fill="none" stroke="var(--navy)"/><path d="M2.5 5.5l2 2 4-5" fill="none" stroke="var(--orange)" stroke-width="1.6"/></svg>CONTRACTORS</li>
      <li><svg width="11" height="11" viewBox="0 0 11 11"><rect x=".5" y=".5" width="10" height="10" fill="none" stroke="var(--navy)"/><path d="M2.5 5.5l2 2 4-5" fill="none" stroke="var(--orange)" stroke-width="1.6"/></svg>DO-IT-YOURSELF'ERS</li>
      <li><svg width="11" height="11" viewBox="0 0 11 11"><rect x=".5" y=".5" width="10" height="10" fill="none" stroke="var(--navy)"/><path d="M2.5 5.5l2 2 4-5" fill="none" stroke="var(--orange)" stroke-width="1.6"/></svg>HOME AND OFFICE SUPPLIES</li>
    </ul>

    <p class="abs extra-band">We ALSO have 60' bucket/chipper trucks,<br>as well as 12", 14", &amp; 18" chippers for rent<br>at an affordable price</p>

    <svg class="abs" style="left:230px;top:420px" width="471" height="80" viewBox="0 0 471 80" aria-hidden="true">
      <path d="M55 0 H471 V80 H0 Z" fill="#4a4c4f"/>
      <path d="M55 0 L0 80 H28 L80 0 Z" fill="var(--navy)"/>
    </svg>

    <div class="abs thumb" role="img" aria-label="Photo of two Dov skid steer loaders" style="left:262px;width:132px;background:linear-gradient(160deg,#b7c4cf,#c9a436 55%,#5c5a52)"></div>
    <div class="abs thumb" role="img" aria-label="Photo of a Dulsant wood chipper" style="left:406px;width:137px;background:linear-gradient(160deg,#9aa37c,#d8781f 50%,#6a5b3c)"></div>
    <div class="abs thumb" role="img" aria-label="Photo of a Plavek cut-off saw in use" style="left:553px;width:135px;background:linear-gradient(160deg,#9c9f9a,#e4742a 50%,#6a6a66)"></div>

    <div class="abs contact-label">GET IN TOUCH</div>
    <div class="abs contact-line" style="top:424px">
      <svg width="18" height="18" viewBox="0 0 18 18"><circle cx="9" cy="9" r="8" fill="none" stroke="var(--navy)" stroke-width="1.5"/><path d="M6 5c-.8.6-.6 2 .6 3.8s2.6 3 3.8 2.9l1-1-1.5-1.3-.8.6c-.6-.3-1.6-1.3-1.9-2l.6-.8L6.7 4.9z" fill="var(--navy)"/></svg>
      (000) 000-000
    </div>
    <div class="abs contact-line contact-line--mail" style="top:454px">
      <svg width="18" height="18" viewBox="0 0 18 18"><circle cx="9" cy="9" r="8" fill="none" stroke="var(--navy)" stroke-width="1.5"/><rect x="5" y="6" width="8" height="6" fill="none" stroke="var(--navy)" stroke-width="1.2"/><path d="M5 6l4 3 4-3" fill="none" stroke="var(--navy)" stroke-width="1.2"/></svg>
      info@youremail.com
    </div>

    <div class="abs front-web">
      <svg width="16" height="16" viewBox="0 0 16 16"><circle cx="8" cy="8" r="7" fill="none" stroke="#fff" stroke-width="1.3"/><ellipse cx="8" cy="8" rx="3" ry="7" fill="none" stroke="#fff" stroke-width="1.1"/><path d="M1 8h14" stroke="#fff" stroke-width="1.1"/></svg>
      WWW.YOURWEBSITE.COM
    </div>
  </section>

  <!-- Back -->
  <section class="card card--back" aria-label="Postcard back">
    <div class="abs back-photo" role="img" aria-label="Faded photo of a row of bucket trucks" style="background:linear-gradient(180deg,#f3f4f5 0%,#e3e5e7 50%,#eef0f1 100%)"></div>
    <svg class="abs" style="left:0;top:110px" width="372" height="340" viewBox="0 0 372 340" aria-hidden="true">
      <path d="M350 20 C372 120 368 240 340 340 H356 C384 240 388 120 364 20 Z" fill="var(--orange)"/>
      <path d="M364 20 C388 120 384 240 356 340 H372 V20 Z" fill="#fff"/>
    </svg>
    <svg class="abs back-head" viewBox="0 0 380 130" aria-hidden="true">
      <path d="M0 0 H352 L372 125 H0 Z" fill="var(--navy)"/>
      <path d="M0 125 H372 L373 130 H0 Z" fill="#b5b7ba"/>
    </svg>

    <div class="abs brand head-brand">
      <span class="brand__dot"></span>
      <div>
        <div class="brand__name" style="font-size:21px;color:#fff">FIELDLINE</div>
        <div class="brand__sub" style="font-size:10px;color:#fff">RENTALS</div>
      </div>
    </div>
    <div class="abs head-copy">
      <div class="head-copy__lead">WELL MAINTAINED<br>AND NEW EQUIPMENT</div>
      <div class="head-copy__new">NEW LOCATION</div>
    </div>

    <svg class="abs" style="left:38px;top:136px" width="44" height="38" viewBox="0 0 44 38" aria-hidden="true">
      <circle cx="9" cy="28" r="6" fill="none" stroke="var(--navy)" stroke-width="4"/>
      <circle cx="24" cy="31" r="5" fill="none" stroke="var(--navy)" stroke-width="4"/>
      <path d="M13 24 L42 4 M20 27 L42 12" stroke="var(--navy)" stroke-width="4" stroke-linecap="round"/>
    </svg>

    <div class="abs coupon">
      <div class="coupon__big">10% OFF</div>
      <div class="coupon__note">10% off on any equipment</div>
      <div class="coupon__exp">Expires June 2018</div>
    </div>

    <div class="abs call">Call today with any question(s)</div>
    <div class="abs call-phone">
      <svg width="22" height="22" viewBox="0 0 18 18"><circle cx="9" cy="9" r="8" fill="none" stroke="var(--navy)" stroke-width="1.5"/><path d="M6 5c-.8.6-.6 2 .6 3.8s2.6 3 3.8 2.9l1-1-1.5-1.3-.8.6c-.6-.3-1.6-1.3-1.9-2l.6-.8L6.7 4.9z" fill="var(--navy)"/></svg>
      (000) 000-000
    </div>
    <div class="abs hours-label">Office Hours</div>
    <div class="abs hours"><b>Mon - Sat</b> 8am - 5pm <b>Closed</b> Sundays</div>

    <div class="abs return-addr">Fieldline Rentals<br>Your Address<br>Your Town</div>
    <div class="abs postage">PRSRT STD<br>ECRWSS<br>U.S. Postage<br>PAID<br>EDDM RETAIL</div>
    <div class="abs mail-box">
      <span class="mail-box__route">*****************ECRWSS****</span>
      <span class="mail-box__to">Local<br>Postal Customer</span>
    </div>
    <div class="abs equip-art" role="img" aria-label="Illustration of a tiller, a stump grinder and a Dulsant chipper"></div>
    <div class="abs back-web">WWW.YOURWEBSITE.COM</div>

    <div class="abs back-foot-rule"></div>
    <div class="abs back-foot">
      <span class="back-foot__claim">WE WILL BEAT ANY COMPETITORS PRICE</span>
      <div class="socials" aria-label="Social media"><span></span><span></span><span></span><span></span></div>
    </div>
  </section>

</main>
</body>
</html>
```